Tavok Construction we build lodges in Botswana

We need a Design Layout only with Categories where we can update each projects photos.... We have a web address and a host - tavok.construction

```html
<!DOCTYPE html>
<html lang="en">
<head>
<meta charset="utf-8">
<title>Tavok Construction – Lodge Construction &amp; Building</title>
<link rel="stylesheet" href="https://fonts.googleapis.com/css2?family=Montserrat:wght@400;600;700;800&family=Roboto:wght@400;500;700&display=swap">
<style>
:root{
  --red:#e8161b;
  --red-deep:#c80d10;
  --black:#000;
  --white:#fff;
  --ink:#111;
  --blue:#2a6fb0;
  --blue-light:#4f8fc9;
  --sky-text:#3d8fd0;
}
*{box-sizing:border-box;margin:0;padding:0}
html,body{width:1200px;height:3629px;overflow:hidden}
body{font-family:"Montserrat",sans-serif;background:var(--white);color:var(--ink);position:relative}

/* Hero */
.hero{position:absolute;left:0;top:0;width:1200px;height:658px;
  background:linear-gradient(180deg,#2b3438 0%,#1c2326 40%,#3a2c22 70%,#1a1512 100%);}
.hero-photo{position:absolute;inset:0;
  background:radial-gradient(ellipse 380px 240px at 760px 470px,rgba(150,90,50,.55),transparent 70%),
             linear-gradient(90deg,rgba(10,14,12,.85) 0%,rgba(10,14,12,.2) 35%,rgba(10,14,12,.2) 75%,rgba(10,14,12,.85) 100%);}
.brand-box{position:absolute;left:53px;top:0;width:230px;height:194px;background:var(--white);
  display:flex;flex-direction:column;align-items:center;justify-content:center;gap:14px}
.brand-mark{width:56px;height:56px;background:var(--red)}
.brand-name{font-family:"Montserrat",sans-serif;font-weight:700;font-size:17px;color:var(--blue)}
.main-nav{position:absolute;top:50px;right:58px;display:flex;align-items:center}
.main-nav a{color:var(--white);text-decoration:none;font-size:13px;font-weight:400;letter-spacing:.5px;
  text-transform:uppercase;width:108px;text-align:center;position:relative;padding:8px 0}
.main-nav a.is-active::after{content:"";position:absolute;left:18px;right:18px;bottom:-8px;height:4px;background:var(--red)}
.main-nav a.nav-contact{background:var(--red);border-radius:18px;width:118px;margin-left:30px;padding:9px 0}
.hero-kicker{position:absolute;left:58px;top:356px;font-size:12px;font-weight:600;letter-spacing:1px;color:var(--sky-text);text-transform:uppercase;white-space:nowrap}
.hero-title{position:absolute;left:56px;top:380px;font-size:56px;line-height:60px;font-weight:800;color:var(--white);text-transform:uppercase;white-space:nowrap}
.hero-btn{position:absolute;left:58px;top:515px;width:214px;height:48px;border-radius:10px;
  background:linear-gradient(90deg,var(--blue),var(--blue-light));color:var(--white);font-size:14px;font-weight:600;
  letter-spacing:1.5px;display:flex;align-items:center;justify-content:center;text-decoration:none}

/* Project tour sections */
.tour{position:absolute;left:0;width:1200px;height:649px}
.tour.light{background:var(--white);color:var(--ink)}
.tour.dark{background:var(--black);color:var(--white)}
.tour-title{position:absolute;font-size:40px;font-weight:800;text-transform:uppercase;line-height:1;white-space:nowrap}
.tour-rule{position:absolute;height:9px}
.light .tour-rule{background:var(--black)}
.dark .tour-rule{background:var(--white)}
.tour-body{position:absolute;width:666px;font-size:12px;line-height:15.5px;letter-spacing:-.1px}
.tour-body p{margin-bottom:11px}
.tour-body h3{font-size:12px;font-weight:700;margin-bottom:11px}
.tour-body strong{font-weight:700}
.read-more{position:absolute;width:182px;height:42px;border-radius:21px;display:flex;align-items:center;
  font-size:12.5px;font-weight:700;letter-spacing:.5px;text-decoration:none;overflow:hidden}
.light .read-more{background:var(--black);color:var(--white)}
.dark .read-more{background:var(--white);color:var(--black)}
.read-more span{flex:1;padding-left:34px}
.read-more i{width:34px;height:42px;background:var(--red);border-radius:0 21px 21px 0;display:flex;align-items:center;justify-content:center}
.photo-lake{position:absolute;left:726px;width:474px;height:422px;
  background:linear-gradient(90deg,#ffffff 0%,rgba(255,255,255,0) 22%),
             linear-gradient(180deg,#e8eef0 0%,#8a9da3 35%,#4b6a6a 60%,#1f4e52 80%,#2b5b5c 100%)}
.photo-night{position:absolute;left:0;width:475px;height:447px;
  background:radial-gradient(ellipse 200px 120px at 220px 300px,rgba(190,100,40,.6),transparent 70%),
             linear-gradient(180deg,#0f1a33 0%,#27345a 40%,#2a2326 75%,#0a0a0a 100%)}

/* Footer */
.site-footer{position:absolute;left:0;top:3243px;width:1200px;height:386px;color:var(--white);
  background:linear-gradient(180deg,var(--red) 0%,#e01418 60%,var(--red-deep) 100%);font-family:"Roboto",sans-serif}
.footer-col{position:absolute;top:80px}
.footer-col h4{font-size:18px;font-weight:700;margin-bottom:20px}
.footer-col ul{list-style:none;font-size:15.5px;line-height:19px}
.footer-col.office{right:58px;text-align:right;font-size:15.5px;line-height:19px}
.footer-brand{position:absolute;left:58px;top:198px;display:flex;align-items:center;gap:10px}
.footer-brand .mark{width:34px;height:34px;background:var(--white)}
.footer-brand .name{font-family:"Roboto",sans-serif;font-weight:700;font-size:18px}
.social{display:flex;gap:8px}
.social span{width:28px;height:28px;border-radius:50%;background:var(--black)}
.copyright{position:absolute;left:0;right:0;top:345px;text-align:center;font-size:13px}
</style>
</head>
<body>

<header class="hero">
  <div class="hero-photo" role="img" aria-label="Photo of a wooden lodge among tall pine trees at dusk"></div>
  <div class="brand-box">
    <div class="brand-mark"></div>
    <div class="brand-name">Tavok Construction</div>
  </div>
  <nav class="main-nav">
    <a href="#" class="is-active">Home</a>
    <a href="#">About</a>
    <a href="#">Product</a>
    <a href="#">Partners</a>
    <a href="#" class="nav-contact">Contact</a>
  </nav>
  <p class="hero-kicker">Construction company based in the Okavango Delta and specialize in lodge building</p>
  <h1 class="hero-title">Lodge Construction<br>&amp; Building</h1>
  <a href="#" class="hero-btn">PRODUCTS</a>
</header>

<!-- Project 1 -->
<section class="tour light" style="top:658px">
  <h2 class="tour-title" style="left:58px;top:92px">Marula State Park Tour</h2>
  <div class="tour-rule" style="left:0;width:726px;top:152px"></div>
  <div class="photo-lake" style="top:142px" role="img" aria-label="Photo of a lakeside lodge below mountain peaks"></div>
  <div class="tour-body" style="left:58px;top:194px">
    <p>Halvern Construction has erected scaffolding to begin to repair the brick and cast stone. Built in 1930, this is the first time that the masonry façade of the building has been repaired. During 2019, windows and other exterior historic elements will be removed, repaired and reinstalled. The restoration is a meticulous effort, meeting federal preservation standards.</p>
    <h3>Construction Fencing</h3>
    <p>The construction fence around the Seminary and former swimming pool building has been moved to enclose the adjacent upper parking lot. This is for construction mobilization, exterior restoration of the brick and cast stone, and public safety. It does not represent the lease footprint of the Lodge and is only temporary. The construction fence is will be fully removed when the Lodge opens in 2020.</p>
    <p><strong>Please Note:</strong> Access to the gymnasium is from the north parking lot.</p>
    <p>The construction fence is only temporary and will be fully removed when the Lodge opens in 2020.</p>
    <p>November 28, 2017 - Morrow Real Estate today released the first renderings of the Lodge at Marula Park. Slated to open in 2020, the Romanesque Revival architecture and Art Deco interiors will be restored to federal standards for the public to enjoy for the first time in history. As a seminary, the building was not open to the public and when purchased by the state in 1976, it was mostly shuttered for over 40-years. As a Lodge, it will provide a quintessential Pacific Northwest experience with a décor that embraces the peaceful setting.<br>For updated information regarding this project, please visit: <strong>www.thelodgeatmarula.com</strong></p>
  </div>
  <a href="#" class="read-more" style="left:58px;top:544px"><span>READ MORE</span><i><svg width="10" height="14" viewBox="0 0 10 14"><path d="M2 1l6 6-6 6" fill="none" stroke="#fff" stroke-width="2.5"/></svg></i></a>
</section>

<!-- Project 2 -->
<section class="tour dark" style="top:1307px">
  <h2 class="tour-title" style="left:484px;top:78px">Marula State Park Tour</h2>
  <div class="tour-rule" style="left:484px;width:716px;top:140px"></div>
  <div class="photo-night" style="top:121px" role="img" aria-label="Photo of a lit timber lodge under a night sky"></div>
  <div class="tour-body" style="left:484px;top:182px">
    <p>Halvern Construction has erected scaffolding to begin to repair the brick and cast stone. Built in 1930, this is the first time that the masonry façade of the building has been repaired. During 2019, windows and other exterior historic elements will be removed, repaired and reinstalled. The restoration is a meticulous effort, meeting federal preservation standards.</p>
    <h3>Construction Fencing</h3>
    <p>The construction fence around the Seminary and former swimming pool building has been moved to enclose the adjacent upper parking lot. This is for construction mobilization, exterior restoration of the brick and cast stone, and public safety. It does not represent the lease footprint of the Lodge and is only temporary. The construction fence is will be fully removed when the Lodge opens in 2020.</p>
    <p><strong>Please Note:</strong> Access to the gymnasium is from the north parking lot.</p>
    <p>The construction fence is only temporary and will be fully removed when the Lodge opens in 2020.</p>
    <p>November 28, 2017 - Morrow Real Estate today released the first renderings of the Lodge at Marula Park. Slated to open in 2020, the Romanesque Revival architecture and Art Deco interiors will be restored to federal standards for the public to enjoy for the first time in history. As a seminary, the building was not open to the public and when purchased by the state in 1976, it was mostly shuttered for over 40-years. As a Lodge, it will provide a quintessential Pacific Northwest experience with a décor that embraces the peaceful setting.<br>For updated information regarding this project, please visit: <strong>www.thelodgeatmarula.com</strong></p>
  </div>
  <a href="#" class="read-more" style="left:484px;top:528px"><span>READ MORE</span><i><svg width="10" height="14" viewBox="0 0 10 14"><path d="M2 1l6 6-6 6" fill="none" stroke="#fff" stroke-width="2.5"/></svg></i></a>
</section>

<!-- Project 3 -->
<section class="tour light" style="top:1955px">
  <h2 class="tour-title" style="left:58px;top:82px">Marula State Park Tour</h2>
  <div class="tour-rule" style="left:0;width:726px;top:142px"></div>
  <div class="photo-lake" style="top:137px" role="img" aria-label="Photo of a lakeside lodge below mountain peaks"></div>
  <div class="tour-body" style="left:58px;top:184px">
    <p>Halvern Construction has erected scaffolding to begin to repair the brick and cast stone. Built in 1930, this is the first time that the masonry façade of the building has been repaired. During 2019, windows and other exterior historic elements will be removed, repaired and reinstalled. The restoration is a meticulous effort, meeting federal preservation standards.</p>
    <h3>Construction Fencing</h3>
    <p>The construction fence around the Seminary and former swimming pool building has been moved to enclose the adjacent upper parking lot. This is for construction mobilization, exterior restoration of the brick and cast stone, and public safety. It does not represent the lease footprint of the Lodge and is only temporary. The construction fence is will be fully removed when the Lodge opens in 2020.</p>
    <p><strong>Please Note:</strong> Access to the gymnasium is from the north parking lot.</p>
    <p>The construction fence is only temporary and will be fully removed when the Lodge opens in 2020.</p>
    <p>November 28, 2017 - Morrow Real Estate today released the first renderings of the Lodge at Marula Park. Slated to open in 2020, the Romanesque Revival architecture and Art Deco interiors will be restored to federal standards for the public to enjoy for the first time in history. As a seminary, the building was not open to the public and when purchased by the state in 1976, it was mostly shuttered for over 40-years. As a Lodge, it will provide a quintessential Pacific Northwest experience with a décor that embraces the peaceful setting.<br>For updated information regarding this project, please visit: <strong>www.thelodgeatmarula.com</strong></p>
  </div>
  <a href="#" class="read-more" style="left:58px;top:536px"><span>READ MORE</span><i><svg width="10" height="14" viewBox="0 0 10 14"><path d="M2 1l6 6-6 6" fill="none" stroke="#fff" stroke-width="2.5"/></svg></i></a>
</section>

<!-- Project 4 -->
<section class="tour dark" style="top:2597px">
  <h2 class="tour-title" style="left:484px;top:76px">Marula State Park Tour</h2>
  <div class="tour-rule" style="left:484px;width:716px;top:138px"></div>
  <div class="photo-night" style="top:121px" role="img" aria-label="Photo of a lit timber lodge under a night sky"></div>
  <div class="tour-body" style="left:484px;top:180px">
    <p>Halvern Construction has erected scaffolding to begin to repair the brick and cast stone. Built in 1930, this is the first time that the masonry façade of the building has been repaired. During 2019, windows and other exterior historic elements will be removed, repaired and reinstalled. The restoration is a meticulous effort, meeting federal preservation standards.</p>
    <h3>Construction Fencing</h3>
    <p>The construction fence around the Seminary and former swimming pool building has been moved to enclose the adjacent upper parking lot. This is for construction mobilization, exterior restoration of the brick and cast stone, and public safety. It does not represent the lease footprint of the Lodge and is only temporary. The construction fence is will be fully removed when the Lodge opens in 2020.</p>
    <p><strong>Please Note:</strong> Access to the gymnasium is from the north parking lot.</p>
    <p>The construction fence is only temporary and will be fully removed when the Lodge opens in 2020.</p>
    <p>November 28, 2017 - Morrow Real Estate today released the first renderings of the Lodge at Marula Park. Slated to open in 2020, the Romanesque Revival architecture and Art Deco interiors will be restored to federal standards for the public to enjoy for the first time in history. As a seminary, the building was not open to the public and when purchased by the state in 1976, it was mostly shuttered for over 40-years. As a Lodge, it will provide a quintessential Pacific Northwest experience with a décor that embraces the peaceful setting.<br>For updated information regarding this project, please visit: <strong>www.thelodgeatmarula.com</strong></p>
  </div>
  <a href="#" class="read-more" style="left:484px;top:527px"><span>READ MORE</span><i><svg width="10" height="14" viewBox="0 0 10 14"><path d="M2 1l6 6-6 6" fill="none" stroke="#fff" stroke-width="2.5"/></svg></i></a>
</section>

<footer class="site-footer">
  <div class="footer-col" style="left:58px">
    <h4>Our Key Services</h4>
    <ul><li>Link Outreach</li><li>Organic Search (SEO)</li></ul>
  </div>
  <div class="footer-brand">
    <div class="mark"></div>
    <div class="name">Tavok Construction</div>
  </div>
  <div class="footer-col" style="left:313px">
    <h4>Locations We Cover (SEO)</h4>
    <ul>
      <li>Birmingham</li><li>Essex</li><li>London</li><li>Manchester</li><li>Stoke-on-Trent</li>
      <li>&raquo;&nbsp; See All Locations We Cover<br>(SEO)</li>
    </ul>
  </div>
  <div class="footer-col" style="left:668px">
    <h4>Connect With Us</h4>
    <div class="social"><span></span><span></span><span></span><span></span><span></span></div>
  </div>
  <div class="footer-col office">
    <h4>Shrewsbury Office</h4>
    <p>Kestrel Digital Ltd, The Granary<br>14 Ashcombe Rd, Bayston Hill<br>Shrewsbury<br>SY3 7QX</p>
    <p style="margin-top:38px">Phone: 01743 000123<br>Email: info@kestreldigital.com</p>
  </div>
  <p class="copyright">© 2018 HOLLIS &amp; CO. All rights reserved.</p>
</footer>

</body>
</html>
```